Consulting company needs Business Cards - rough concept provided

I'm looking for someone to take our business card idea and make is slick and polished - to communicate our high-end, sophisticated, serious consulting business. We have a rough layout we did in-house. We are open to ideas on repo-ing elements, adjusting sizes, typefaces etc... within the general concept we've already come up with. We want it to be super-clean and sophisticated. We want to keep the white backgrounds, and blue brand colors. Our goal is to print with painted blue edges on thick cardstock. Thank you!!

```html
<!DOCTYPE html>
<html lang="en">
<head>
<meta charset="utf-8">
<title>Tallbridge Business Card</title>
<link rel="stylesheet" href="https://fonts.googleapis.com/css2?family=Archivo:wght@300;400;700;800&display=swap">
<style>
  :root {
    --brand-blue: #009cdc;
    --paper: #ffffff;
    --backdrop: #cccccc;
    --muted: #a8a8a8;
  }
  * { box-sizing: border-box; margin: 0; padding: 0; }
  html, body {
    width: 1200px; height: 1000px; overflow: hidden;
    background: var(--backdrop);
    font-family: "Archivo", "Helvetica Neue", Arial, sans-serif;
  }
  .card {
    position: absolute; left: 266px; width: 668px; height: 380px;
  }
  .card--front { top: 86px; background: var(--paper); }
  .card--back { top: 527px; background: var(--brand-blue); color: var(--paper); }

  .wordmark { position: absolute; left: 0; top: 0; width: 668px; height: 90px; display: block; }
  .wordmark text { font-family: "Archivo", Arial, sans-serif; font-weight: 800; fill: var(--brand-blue); }

  .holder-name {
    position: absolute; left: 44px; top: 154px;
    font-size: 20px; font-weight: 700; color: var(--brand-blue); letter-spacing: 0.2px;
  }
  .holder-title {
    position: absolute; left: 44px; top: 183px;
    font-size: 12.5px; font-weight: 400; color: var(--muted); letter-spacing: 2.6px;
  }
  .dot-grid {
    position: absolute; left: 44px; top: 238px; width: 298px; height: 86px;
    background-image: linear-gradient(var(--brand-blue), var(--brand-blue));
    background-size: 9px 9px;
    background-repeat: space;
  }
  .contact {
    position: absolute; left: 365px; top: 231px;
    list-style: none; font-size: 18.5px; line-height: 24.6px; color: var(--brand-blue); font-weight: 400;
  }

  .dot-rule {
    height: 7px;
    background-image: linear-gradient(var(--paper), var(--paper));
    background-size: 7px 7px;
    background-repeat: space no-repeat;
  }
  .dot-rule--top { position: absolute; left: 63px; top: 86px; width: 540px; }
  .mission {
    position: absolute; left: 63px; top: 101px; width: 540px;
    font-size: 27px; line-height: 36px; font-weight: 300;
  }
  .mission__line { text-align: justify; text-align-last: justify; white-space: nowrap; }
  .mission b { font-weight: 700; }
  .mission__line--last { display: flex; align-items: center; gap: 26px; }
  .mission__line--last .dot-rule { flex: 1; margin-top: 4px; }
  .site { position: absolute; left: 66px; top: 259px; width: 538px; height: 62px; display: block; }
  .site text { font-family: "Archivo", Arial, sans-serif; font-weight: 800; fill: var(--paper); }
</style>
</head>
<body>
  <section class="card card--front">
    <svg class="wordmark" viewBox="0 0 668 90" aria-label="Tallbridge">
      <text x="0" y="86" font-size="118" textLength="668" lengthAdjust="spacingAndGlyphs">TALLBRIDGE</text>
    </svg>
    <h1 class="holder-name">DANA WHITFIELD</h1>
    <p class="holder-title">BRAND CONSULTANT</p>
    <div class="dot-grid" aria-hidden="true"></div>
    <ul class="contact">
      <li>4820 Harbor Lane, Ste 210</li>
      <li>Fairview, CA 90210</li>
      <li>(555) 014 2290</li>
      <li>dana@tallbridge.com</li>
    </ul>
  </section>

  <section class="card card--back">
    <div class="dot-rule dot-rule--top" aria-hidden="true"></div>
    <div class="mission">
      <div class="mission__line"><b>We</b> <b>help</b> [target demographic] <b>achieve</b></div>
      <div class="mission__line" style="letter-spacing:3px">[desired emotional outcome] <b>by</b></div>
      <div class="mission__line" style="letter-spacing:-0.6px">[our unique approach] <b>because</b> [our brand</div>
      <div class="mission__line mission__line--last"><span>beliefs]</span><span class="dot-rule" aria-hidden="true"></span></div>
    </div>
    <svg class="site" viewBox="0 0 538 62" aria-label="tallbridge.com">
      <text x="0" y="58" font-size="80" textLength="538" lengthAdjust="spacingAndGlyphs">TALLBRIDGE.COM</text>
    </svg>
  </section>
</body>
</html>
```